Business Card Design Project

I am looking for a classy business card design for a product design consultancy. We specialize in Product Design, Prototyping, and Manufacturing Consulting. Products that we design range from consumer electronics to household products all the way to sporting goods. We are based in Arizona and called "Heron Design Works." We like to have fun and goof off as much as we like to create new products. We are young and energetic so we would like our business cards to reflect that. We already have a logo that we would like to implement into the card design. A plain rectangular business card is boring so feel free to get creative, but please, no avocado shaped cards (it's far too literal). Also feel free to play around with textured card stocks or plastic. The final design that we choose will pay attention to all of the little details. Our cards will need to be 2 sided. We're giving you guys free reign to design as you would like. Please have fun with this, it will reflect in our business card.

Thanks guys,
Heron Design Works Team

Industry/Entity Type

Electronics

Requirements
Must have
• We would like to have a spot UV coating somewhere on the business card design if possible.
Nice to have
• Let's see some designs with custom shapes rather than typical rectangular business cards but please no avocado shaped cards, thanks. Also play around with textured card socks.

```html
<!DOCTYPE html>
<html lang="en">
<head>
<meta charset="utf-8">
<title>Heron Design Works – Business Card</title>
<link href="https://fonts.googleapis.com/css2?family=Questrial&display=swap" rel="stylesheet">
<style>
  :root {
    --page-bg: #efece6;
    --card-white: #ffffff;
    --circle-grey: #ececec;
    --circle-light: #f7f7f7;
    --brand-green: #74b92f;
    --brand-green-light: #8cc63f;
    --brand-green-dark: #5e9f22;
    --ink: #444444;
    --ink-soft: #666666;
    --white: #ffffff;
  }
  * { box-sizing: border-box; margin: 0; padding: 0; }
  html, body { width: 1200px; height: 1024px; overflow: hidden; }
  body {
    background: var(--page-bg);
    font-family: "Questrial", "Century Gothic", sans-serif;
    display: flex;
    flex-direction: column;
    align-items: center;
    justify-content: center;
    gap: 24px;
  }
  .card {
    position: relative;
    width: 840px;
    height: 480px;
    border-radius: 34px;
    overflow: hidden;
    box-shadow: 0 6px 18px rgba(0,0,0,0.12);
  }

  /* Back: contact side */
  .card--contact { background: var(--card-white); }
  .card--contact .decor-circle {
    position: absolute;
    right: -60px;
    top: -250px;
    width: 560px;
    height: 560px;
    border-radius: 50%;
    background: var(--circle-grey);
  }
  .card--contact .decor-circle-inner {
    position: absolute;
    right: 40px;
    top: -40px;
    width: 250px;
    height: 250px;
    border-radius: 50%;
    background: var(--circle-light);
  }
  .brand {
    display: flex;
    align-items: center;
    gap: 14px;
    color: var(--brand-green);
  }
  .brand-dot {
    border-radius: 50%;
    background: currentColor;
    flex: none;
  }
  .brand-name { font-weight: 400; letter-spacing: 1px; white-space: nowrap; }

  .card--contact .brand {
    position: absolute;
    left: 60px;
    top: 150px;
  }
  .card--contact .brand-dot { width: 46px; height: 46px; }
  .card--contact .brand-name { font-size: 50px; }

  .person {
    position: absolute;
    left: 70px;
    top: 236px;
  }
  .person-name { font-size: 30px; color: var(--ink); }
  .person-title { font-size: 24px; color: var(--brand-green); margin-top: 2px; }
  .contact-list {
    list-style: none;
    margin-top: 10px;
  }
  .contact-list li {
    display: flex;
    align-items: center;
    gap: 12px;
    font-size: 22px;
    color: var(--ink);
    line-height: 30px;
  }
  .contact-list svg { width: 18px; height: 18px; flex: none; }

  .contact-band {
    position: absolute;
    left: 0; right: 0; bottom: 0;
    height: 66px;
    background: var(--brand-green-light);
    display: flex;
    align-items: center;
    justify-content: space-between;
    padding: 0 44px 0 70px;
  }
  .web-address { color: var(--white); font-size: 22px; letter-spacing: 1px; }
  .social-links { display: flex; gap: 6px; }
  .social-square {
    width: 26px; height: 26px;
    border-radius: 3px;
    background: var(--white);
    opacity: 0.85;
  }

  /* Front: brand side */
  .card--brand {
    background: radial-gradient(ellipse at 40% 35%, var(--brand-green-light) 0%, var(--brand-green) 55%, var(--brand-green-dark) 100%);
    display: flex;
    flex-direction: column;
    align-items: center;
    justify-content: center;
    gap: 40px;
  }
  .card--brand .brand { color: var(--white); }
  .card--brand .brand-dot { width: 64px; height: 64px; }
  .card--brand .brand-name { font-size: 70px; }
  .services {
    color: var(--white);
    font-size: 19px;
    letter-spacing: 2px;
    text-transform: uppercase;
  }
</style>
</head>
<body>

  <section class="card card--contact" aria-label="Business card contact side">
    <div class="decor-circle"></div>
    <div class="decor-circle-inner"></div>

    <div class="brand">
      <span class="brand-dot"></span>
      <span class="brand-name">Heron Design Works</span>
    </div>

    <div class="person">
      <p class="person-name">Dylan Marsh</p>
      <p class="person-title">President</p>
      <ul class="contact-list">
        <li>
          <svg viewBox="0 0 24 24" aria-hidden="true"><path fill="#74b92f" d="M6.6 10.8a15.1 15.1 0 0 0 6.6 6.6l2.2-2.2a1 1 0 0 1 1-.25 11.4 11.4 0 0 0 3.6.57 1 1 0 0 1 1 1V20a1 1 0 0 1-1 1A17 17 0 0 1 3 4a1 1 0 0 1 1-1h3.5a1 1 0 0 1 1 1c0 1.25.2 2.45.57 3.57a1 1 0 0 1-.25 1z"/></svg>
          480.555.0172
        </li>
        <li>
          <svg viewBox="0 0 24 24" aria-hidden="true"><rect x="6" y="2" width="12" height="20" rx="2" fill="none" stroke="#74b92f" stroke-width="2"/><circle cx="12" cy="18" r="1.2" fill="#74b92f"/></svg>
          602.555.0148
        </li>
        <li>
          <svg viewBox="0 0 24 24" aria-hidden="true"><rect x="2" y="5" width="20" height="14" rx="1.5" fill="#74b92f"/><path d="M3 6l9 7 9-7" fill="none" stroke="#fff" stroke-width="1.6"/></svg>
          dylan@herondesignworks.com
        </li>
      </ul>
    </div>

    <div class="contact-band">
      <span class="web-address">www.herondesignworks.com</span>
      <div class="social-links" aria-label="Social profiles">
        <span class="social-square"></span>
        <span class="social-square"></span>
        <span class="social-square"></span>
      </div>
    </div>
  </section>

  <section class="card card--brand" aria-label="Business card brand side">
    <div class="brand">
      <span class="brand-dot"></span>
      <span class="brand-name">Heron Design Works</span>
    </div>
    <p class="services">Product Development | Prototyping | Manufacturing Consulting</p>
  </section>

</body>
</html>
```